Professional IT Company Letterhead

We need a new letterhead design to incorporate our new login and business card design recently received here on Sketch Guild. We want the same look and feel as the other two accepted projects. We want a professional and clean design.

Target Market(s)

Medical/Dental and Professional Services Businesses (CPA, Attorney, Architect etc)

Industry/Entity Type

Business

Requirements
Must have
• Clean and professional, consistent brand with our current design of our new logo and business cards.
Nice to have
• Would like to also be able to use the design on our newsletter header

```html
<!DOCTYPE html>
<html lang="en">
<head>
<meta charset="utf-8">
<title>Tidewell Letterhead</title>
<link href="https://fonts.googleapis.com/css2?family=Arimo:wght@400;700&display=swap" rel="stylesheet">
<style>
  :root {
    --brand-blue: #1e9ad6;
    --deep-blue: #0a74bb;
    --accent-orange: #f7931e;
    --charcoal: #4a4a4c;
    --text-grey: #4d4d4f;
    --icon-grey: #58585a;
    --paper: #ffffff;
  }
  html, body {
    margin: 0;
    padding: 0;
    overflow: hidden;
    background: var(--paper);
  }
  .letterhead {
    position: relative;
    width: 927px;
    height: 1200px;
    background: var(--paper);
    overflow: hidden;
    font-family: "Arimo", Arial, sans-serif;
  }
  .brand-name {
    position: absolute;
    top: 64px;
    left: 0;
    width: 100%;
    text-align: center;
    margin: 0;
    font-size: 52px;
    font-weight: 700;
    letter-spacing: -1px;
    color: var(--brand-blue);
    line-height: 1;
  }
  .corner-shapes {
    position: absolute;
    left: 0;
    bottom: 0;
  }
  .contact-row {
    position: absolute;
    top: 1142px;
    left: 0;
    width: 100%;
    height: 16px;
    font-size: 11px;
    color: var(--text-grey);
  }
  .contact-item {
    position: absolute;
    display: flex;
    align-items: center;
    gap: 6px;
    white-space: nowrap;
  }
  .contact-item svg { flex: none; }
  .contact-address { left: 200px; }
  .contact-email { left: 462px; }
  .contact-web { left: 623px; }
  .contact-phone { left: 777px; }
  .footer-bar {
    position: absolute;
    left: 195px;
    right: 0;
    bottom: 0;
    height: 17px;
    background: var(--charcoal);
  }
</style>
</head>
<body>
<div class="letterhead">
  <h1 class="brand-name">tidewell</h1>

  <div class="contact-row">
    <div class="contact-item contact-address">
      <svg width="11" height="11" viewBox="0 0 12 12"><circle cx="6" cy="6" r="6" fill="var(--icon-grey)"/><path d="M6 2.6a2.2 2.2 0 0 0-2.2 2.2C3.8 6.5 6 9.2 6 9.2s2.2-2.7 2.2-4.4A2.2 2.2 0 0 0 6 2.6z" fill="#fff"/><circle cx="6" cy="4.8" r="0.8" fill="var(--icon-grey)"/></svg>
      <span>58 Harbour Lane, Easton QLD 4021</span>
    </div>
    <div class="contact-item contact-email">
      <svg width="11" height="11" viewBox="0 0 12 12"><circle cx="6" cy="6" r="6" fill="var(--icon-grey)"/><rect x="3" y="4" width="6" height="4" rx="0.6" fill="#fff"/></svg>
      <span>hello@tidewellsys.com</span>
    </div>
    <div class="contact-item contact-web">
      <svg width="11" height="11" viewBox="0 0 12 12"><circle cx="6" cy="6" r="5.4" fill="none" stroke="var(--icon-grey)" stroke-width="1.2"/><circle cx="6" cy="6" r="3" fill="none" stroke="var(--icon-grey)" stroke-width="0.8"/><path d="M3 6h6M6 3v6" stroke="var(--icon-grey)" stroke-width="0.8"/></svg>
      <span>www.tidewellsys.com</span>
    </div>
    <div class="contact-item contact-phone">
      <svg width="11" height="11" viewBox="0 0 12 12"><circle cx="6" cy="6" r="6" fill="var(--icon-grey)"/><path d="M4.2 3c.3 0 .9 1.2.9 1.4 0 .3-.5.5-.5.8.2.8 1.3 1.9 2.1 2.1.3 0 .5-.5.8-.5.2 0 1.4.6 1.4.9 0 .6-.6 1.2-1.2 1.2C5.6 8.9 3.1 6.4 3 4.3 3 3.6 3.6 3 4.2 3z" fill="#fff"/></svg>
      <span>+11 (52) 408 719</span>
    </div>
  </div>

  <svg class="corner-shapes" width="215" height="220" viewBox="0 0 215 220" aria-hidden="true">
    <polygon points="0,2 198,202 0,202" fill="var(--deep-blue)"/>
    <polygon points="195,201 213,220 177,220" fill="var(--accent-orange)"/>
  </svg>
  <div class="footer-bar"></div>
</div>
</body>
</html>
```